Harrowgate Estates Business Card for Apartment Buildings

Create business cards for resident managers who run apartment buildings. The audience is the public who are searching for apartment rentals, and current residents who live at the apartment building. Key design element will be incorporating the company logo, however, the logo cannot dominate. The building name and manager name are more important than the logo. Current business card design leaves little room for copy, so we may need to reduce the size on the current card to allow for more space for copy.

Target Market(s)

Adults 18-65 years of age, who are looking for an apartment rental, plus current residents who live at our apartment buildings.

Industry/Entity Type

Property Management

Contact Information for Business Card

A major design element will be use of the company logo. Important property and manager contact information must be part of the design. The size of the logo will need to be reduced to make room for building and manager contact copy.

Font styles to use
Sans Serif

Colors
3176b5
000000
959595
ffffff

Requirements
Must have
• 1) Incorporate the company logo.
• 2) Use the company colors (dark blue, black/grey, over white).
• 3) FEATURE THE BUILDING NAME
• 4) FEATURE THE MANAGER NAME
• 5) The company name is less important than BUILDING and MANAGER
• 6) Manager contact information
• **SEE ATTACHED CREATIVE BRIEF**
Nice to have
• 1) Back of card logo watermark
• 2) Ability to write notes on back of carfd
Should not have
• Avoid letting the company logo dominate the card, the building name and manager are more important than the company logo.

```html
<!DOCTYPE html>
<html lang="en">
<head>
<meta charset="utf-8">
<title>Harrowgate Estates – Resident Manager Card</title>
<link href="https://fonts.googleapis.com/css2?family=Catamaran:wght@300;400;600;700&display=swap" rel="stylesheet">
<style>
  :root {
    --brand-blue: #1a6aab;
    --charcoal: #444446;
    --text-grey: #555558;
    --rule-grey: #8c8c8c;
    --paper: #ffffff;
    --paper-back: #e6e7e8;
    --backdrop: #a4a4a4;
    --watermark: #cfd4d9;
  }
  * { box-sizing: border-box; margin: 0; padding: 0; }
  html, body {
    width: 1200px; height: 1200px; overflow: hidden;
    background: var(--backdrop);
    font-family: "Catamaran", "Helvetica Neue", Arial, sans-serif;
  }
  .card {
    position: absolute; left: 204px; width: 792px; height: 452px;
    overflow: hidden;
  }
  .card--front { top: 92px; background: var(--paper); }
  .card--back { top: 656px; height: 450px; background: var(--paper-back); }

  /* front */
  .front-info { position: absolute; right: 42px; top: 0; text-align: right; }
  .building-name {
    position: absolute; right: 0; top: 36px; white-space: nowrap;
    font-size: 44px; font-weight: 600; color: var(--brand-blue); letter-spacing: 0.2px;
  }
  .address {
    position: absolute; right: 0; top: 100px; white-space: nowrap;
    font-size: 19px; font-weight: 300; line-height: 32px; color: var(--text-grey);
  }
  .manager-name {
    position: absolute; right: 0; top: 176px; white-space: nowrap;
    font-size: 27px; font-weight: 600; color: var(--brand-blue);
  }
  .manager-role {
    position: absolute; right: 0; top: 214px; white-space: nowrap;
    font-size: 19px; font-weight: 400; color: var(--text-grey);
  }
  .contact-list {
    position: absolute; right: 0; top: 262px; list-style: none;
  }
  .contact-list li {
    display: flex; justify-content: flex-end; align-items: center; gap: 14px;
    height: 31px; font-size: 18px; font-weight: 300; color: var(--text-grey); white-space: nowrap;
  }
  .contact-list svg { width: 18px; height: 18px; flex: none; }
  .accent { color: var(--brand-blue); font-weight: 400; }

  .front-brand {
    position: absolute; left: 34px; bottom: 44px;
    display: flex; align-items: center; gap: 14px;
  }
  .brand-dot { width: 38px; height: 38px; border-radius: 50%; background: var(--charcoal); }
  .brand-name {
    font-size: 30px; font-weight: 700; color: var(--brand-blue); line-height: 1; white-space: nowrap;
  }

  /* back */
  .back-brand {
    position: absolute; top: 66px; left: 0; right: 0; text-align: center;
    font-size: 46px; font-weight: 700; color: var(--brand-blue); letter-spacing: 1px; line-height: 1;
  }
  .back-watermark {
    position: absolute; top: 250px; left: 0; right: 0; text-align: center;
    font-size: 64px; font-weight: 700; color: var(--watermark); line-height: 1; white-space: nowrap;
  }
  .note-lines { position: absolute; left: 42px; right: 40px; top: 218px; }
  .note-lines span {
    display: block; height: 1px; background: var(--rule-grey); margin-bottom: 56px;
  }
</style>
</head>
<body>

<section class="card card--front" aria-label="Business card front">
  <div class="front-brand">
    <span class="brand-dot"></span>
    <span class="brand-name">Harrowgate Estates</span>
  </div>

  <div class="front-info">
    <h1 class="building-name">Linden Court Apartments</h1>
    <p class="address">2450-2462 Orchard Avenue<br>Westbrook, CA 92318</p>
    <h2 class="manager-name">Marisol Ortega</h2>
    <p class="manager-role">Resident Manager</p>
    <ul class="contact-list">
      <li>555-310-4821
        <svg viewBox="0 0 24 24" fill="#1a6aab"><path d="M6.6 2.5l3 3.6-1.8 2.4c1.2 2.6 3.2 4.6 5.7 5.8l2.4-1.8 3.6 3-1.6 3.2c-.4.8-1.3 1.1-2.1.9C9.3 17.8 5.2 13.7 3.4 7.2c-.2-.8.1-1.7.9-2.1z"/></svg>
      </li>
      <li>555-310-4822
        <svg viewBox="0 0 24 24" fill="none" stroke="#1a6aab" stroke-width="2.2"><rect x="6" y="3" width="12" height="5"/><rect x="3" y="9" width="18" height="8" rx="1"/><rect x="7" y="14" width="10" height="6" fill="#fff"/></svg>
      </li>
      <li>555-782-9064
        <svg viewBox="0 0 24 24" fill="none" stroke="#1a6aab" stroke-width="2.2"><rect x="6.5" y="2" width="11" height="20" rx="2"/><circle cx="12" cy="18" r="1" fill="#1a6aab"/></svg>
      </li>
      <li>marisol@harrowgateest.com
        <svg viewBox="0 0 24 24" fill="none" stroke="#1a6aab" stroke-width="2"><rect x="3" y="5" width="18" height="14"/><path d="M3 5l9 8 9-8M3 19l7-7M21 19l-7-7"/></svg>
      </li>
      <li><span>www.<span class="accent">harrowgateest</span>.com</span>
        <svg viewBox="0 0 24 24" fill="none" stroke="#1a6aab" stroke-width="2"><circle cx="12" cy="12" r="9"/><ellipse cx="12" cy="12" rx="4" ry="9"/><path d="M3 12h18M5 7h14M5 17h14"/></svg>
      </li>
    </ul>
  </div>
</section>

<section class="card card--back" aria-label="Business card back">
  <div class="back-brand">HARROWGATE ESTATES</div>
  <div class="back-watermark" aria-hidden="true">Harrowgate Estates</div>
  <div class="note-lines" aria-label="Lines for notes">
    <span></span><span></span><span></span><span></span>
  </div>
</section>

</body>
</html>
```